Skincare ..product is Velmorith revolutionary new skincare product that has created a break thru fo

we need a 5x8 dimension mail piece emphasizing Velmorith Body lotion and Face cream.......this will be sent to potential distributors.....Velmorith is a revolutionary new skin care product designed with an encapsulation process at an FDA lab with emphasis on the proprietary blend QPR.....concentrated hemp extract patent pending that penetrates deeper into the skin....creating a significant anti aging effect on the skin!

Target Market(s)

spas and salons ...women 35-65

Industry/Entity Type

Product

Colors
ffffff
acd037

Requirements
Must have
• picture of the body lotion and the face cream FDA lab approved CBD hemp extract formulation.....amazing results...*. Softest daily balm around or softestdailybalmaround.example.....* Great margins for our distribution partners!....*.Hawaiian vacation for top distributors! WWW.Tidelyfornetrix.example
Nice to have
• call 555-314-2708 picture of model on our site.....

```html
<!DOCTYPE html>
<html lang="en">
<head>
<meta charset="utf-8">
<title>Velmorith – Distributor Mailer</title>
<link rel="stylesheet" href="https://fonts.googleapis.com/css2?family=Gelasio:ital,wght@0,400;1,400;1,700&family=Roboto:wght@300;400;700&family=Roboto+Condensed:wght@700&display=swap">
<style>
  :root {
    --teal: #0d6b6b;
    --green: #3bb54a;
    --green-soft: #acd037;
    --white: #ffffff;
    --stage: #9e9e9e;
    --ink: #1e1e1e;
    --logo-grey: #8a8a8a;
    --panel-grey: #e6e6e6;
  }
  * { box-sizing: border-box; margin: 0; padding: 0; }
  html, body { width: 1200px; height: 720px; overflow: hidden; }
  body { background: var(--stage); position: relative; font-family: "Roboto", Arial, sans-serif; }

  .mailer {
    position: absolute; left: 164px; top: 88px;
    width: 872px; height: 544px;
    background: var(--white); overflow: hidden;
  }

  .headline-band {
    position: absolute; left: 0; top: 0; width: 100%; height: 122px;
    background: var(--teal);
  }
  .headline {
    position: absolute; right: 26px; top: 6px;
    font-family: "Gelasio", Georgia, serif; font-weight: 400;
    font-size: 77px; line-height: 1.2; color: var(--white); letter-spacing: -0.5px;
    white-space: nowrap;
  }
  .subhead {
    position: absolute; right: 52px; top: 92px;
    font-family: "Gelasio", Georgia, serif; font-style: italic; font-weight: 700;
    font-size: 13.5px; color: var(--white);
  }

  .claim-band {
    position: absolute; left: 0; top: 124px; width: 100%; height: 38px;
    background: linear-gradient(90deg, #f1f8ea 0%, #b4e0a4 22%, #5cc25f 50%, var(--green) 70%, var(--green) 100%);
  }
  .claim {
    position: absolute; right: 28px; top: 5px;
    font-family: "Gelasio", Georgia, serif; font-style: italic;
    font-size: 21.5px; color: var(--white); letter-spacing: 0.4px; white-space: nowrap;
  }

  .model-photo {
    position: absolute; left: 418px; top: 162px; width: 454px; height: 313px;
    background:
      linear-gradient(180deg, rgba(20,20,20,0.85) 0%, rgba(30,30,30,0.4) 18%, rgba(0,0,0,0) 32%),
      radial-gradient(ellipse at 58% 55%, #e2e2e2 0%, #b5b5b5 35%, #7c7c7c 75%, #5e5e5e 100%);
  }

  .lotion-bottle { position: absolute; left: 36px; top: 27px; width: 168px; height: 400px; z-index: 2; }
  .bottle-pump {
    position: absolute; left: 43px; top: 0; width: 80px; height: 125px;
    border-radius: 6px 6px 4px 4px;
    background: linear-gradient(90deg, #e4e4e4 0%, #fbfbfb 50%, #dcdcdc 100%);
  }
  .bottle-body {
    position: absolute; left: 0; top: 118px; width: 168px; height: 282px;
    border-radius: 46px 46px 20px 20px;
    background: linear-gradient(90deg, #e6e6dc 0%, #f8f8f2 40%, #ecece2 100%);
  }
  .bottle-caption {
    position: absolute; left: 36px; top: 437px; width: 168px;
    text-align: center; color: var(--teal); font-weight: 700; font-size: 12.5px; line-height: 1.3;
  }

  .brand-mark { position: absolute; left: 226px; top: 180px; width: 180px; }
  .brand-dot {
    position: absolute; left: 57px; top: 0; width: 66px; height: 66px;
    border-radius: 50%; background: var(--green-soft);
  }
  .brand-name {
    position: absolute; left: 0; top: 68px; width: 180px; text-align: center;
    font-family: "Roboto", Arial, sans-serif; font-weight: 300;
    font-size: 31px; color: var(--logo-grey);
  }
  .brand-byline {
    position: absolute; left: 0; top: 106px; width: 180px; text-align: center;
    font-size: 8px; color: var(--logo-grey);
  }
  .formula-note {
    position: absolute; left: 226px; top: 300px; width: 180px; text-align: center;
    font-family: "Gelasio", Georgia, serif; font-style: italic;
    font-size: 9.5px; line-height: 1.25; color: var(--teal);
  }

  .jar-caption {
    position: absolute; left: 214px; top: 356px; width: 52px;
    text-align: center; color: var(--teal); font-weight: 700; font-size: 11.5px; line-height: 1.25;
  }
  .face-cream-jar { position: absolute; left: 269px; top: 322px; width: 190px; height: 172px; z-index: 3; }
  .jar-lid {
    position: absolute; left: 8px; top: 0; width: 174px; height: 70px;
    border-radius: 10px 10px 4px 4px;
    background: linear-gradient(90deg, #bdbdbd 0%, #f2f2f2 45%, #b8b8b8 100%);
  }
  .jar-body {
    position: absolute; left: 0; top: 68px; width: 190px; height: 104px;
    border-radius: 6px 6px 14px 14px;
    background: linear-gradient(90deg, #d0d0d0 0%, #f7f7f7 45%, #c8c8c8 100%);
  }

  .site-pill {
    position: absolute; left: 531px; top: 434px; width: 200px; height: 46px;
    border-radius: 50%; background: var(--teal);
    display: flex; align-items: center; justify-content: center;
    color: var(--white); font-family: "Roboto Condensed", Arial, sans-serif; font-weight: 700; font-size: 13px;
  }

  .footer-margins {
    position: absolute; left: 0; top: 475px; width: 476px; height: 69px;
    background: var(--teal); color: var(--white);
    font-size: 19px; padding: 31px 0 0 31px; white-space: nowrap;
  }
  .footer-call {
    position: absolute; left: 476px; top: 475px; width: 156px; height: 69px;
    background: var(--green); color: var(--white);
    text-align: center; font-weight: 700; font-size: 19px; line-height: 1.25; padding-top: 11px;
  }
  .footer-vacation {
    position: absolute; left: 632px; top: 475px; width: 240px; height: 69px;
    background: var(--panel-grey); color: var(--ink);
    font-weight: 700; font-size: 16.5px; line-height: 1.3; padding: 16px 0 0 27px;
  }
  .vacation-line { display: flex; justify-content: space-between; width: 181px; }
</style>
</head>
<body>
  <main class="mailer">
    <header class="headline-band">
      <h1 class="headline">Amazing Results!</h1>
      <p class="subhead">Revolutionary new skincare product</p>
    </header>

    <div class="claim-band">
      <p class="claim">Significant anti aging effect on the skin!</p>
    </div>

    <div class="model-photo" role="img" aria-label="Black and white portrait of a woman in a black cowboy hat"></div>

    <div class="lotion-bottle" role="img" aria-label="Velmorith Hydrating Body Lotion pump bottle, formulated with QPR">
      <span class="bottle-pump"></span>
      <span class="bottle-body"></span>
    </div>
    <p class="bottle-caption">Softest daily<br>balm around!</p>

    <div class="brand-mark">
      <span class="brand-dot"></span>
      <p class="brand-name">Velmorith</p>
      <p class="brand-byline">By Tidelyfornetrix</p>
    </div>
    <p class="formula-note">FDA lab approved CBD hemp<br>extract formulation</p>

    <p class="jar-caption">Face Cream</p>
    <div class="face-cream-jar" role="img" aria-label="Velmorith Face Cream jar with silver lid">
      <span class="jar-lid"></span>
      <span class="jar-body"></span>
    </div>

    <div class="site-pill">www.Tidelyfornetrix.example</div>

    <footer>
      <div class="footer-margins">Great margins for our distribution partners!</div>
      <div class="footer-call">Call<br>555-314-2708</div>
      <div class="footer-vacation">
        <span class="vacation-line"><span>Hawaiian</span><span>vacation</span></span>
        for top distributors!
      </div>
    </footer>
  </main>
</body>
</html>
```